Dog care service needs advertising poster

Our company is Pawfield Haven. We provide care for dogs while their owners are away, either through home visits or a holiday stay in the homes of carefully selected minders. Our existing website & Facebook cover should provide all the colour cues for a poster - namely blues, blondes and grey. We have an existing logo (provided). We can feature the same imagery from our website as I have purchased the rights to the stock images.

www.pawfieldhaven.com.au
www.facebook.com/pawfieldhavenau

This brief is for design of a poster that can be placed in vet surgeries, groomers, on community noticeboards. It should be scalable to print in three sizes, A5, A4 & A3.

We wish to clearly communicate our three areas of service "dog minding, home visits, dog walking".

We would like to have the files ready for upload to Printlorra (or similar) for immediate printing.

Target Market(s)

Dog owners who love their dogs like family.

Industry/Entity Type

Advertising

Font styles to use
Sans Serif

Colors
33a6d7
3276b5

Requirements
Must have
• Logo
• www.pawfieldhaven.com.au
• Telephone number
• Three services - Dog Minding, Home Visits, Dog Walking
Nice to have
• use of our existing stock photography to highlight the three areas of service - Dog minding, home visits, dog walking. Existing colour palette - blues, blondes and grey.
• Text that can be used:
• Western Sydney’s complete dog care service.
• Dog Minding - Your dog stays in the home of one of our carefully selected minders.Treated like part of the family, they enjoy all the creature comforts they are used to.
• Home Visits - We visit your dog at your home for feeding, walking and playtime. Short of long visits available.
• Dog Walking - If you can't walk your dog for any reason we are here to help. 1/2 hour or hourly walks available.
• Contact us today for a tailored package to meet your needs.
Should not have
• Any additional illustrations beyond the logo.

```html
<!DOCTYPE html>
<html lang="en">
<head>
<meta charset="utf-8">
<title>Pawfield Haven – Poster</title>
<link href="https://fonts.googleapis.com/css2?family=Anton&family=Arimo:wght@400&family=Mulish:wght@600&display=swap" rel="stylesheet">
<style>
  :root {
    --stage: #e9e6e1;
    --paper: #ffffff;
    --slate: #434d5c;
    --band-blue: #389fd8;
    --brand-blue: #33a6d7;
    --deep-blue: #3276b5;
    --label-grey: #4a5363;
    --white: #ffffff;
  }
  * { margin: 0; padding: 0; box-sizing: border-box; }
  html, body {
    width: 913px; height: 1200px; overflow: hidden;
    background: var(--stage);
  }
  .poster {
    position: absolute; left: 120px; top: 125px;
    width: 673px; height: 950px;
    background: var(--paper);
    overflow: hidden;
  }
  .header { position: absolute; left: 0; top: 0; width: 673px; height: 193px; }
  .brand-mark {
    position: absolute; left: 195px; top: 58px;
    width: 64px; height: 64px; border-radius: 50%;
    background: var(--slate);
  }
  .brand-name {
    position: absolute; left: 285px; top: 44px;
    font-family: "Mulish", sans-serif; font-weight: 600;
    font-size: 36px; line-height: 37px; color: var(--slate);
    letter-spacing: -0.3px;
  }
  .brand-tagline {
    position: absolute; left: 322px; top: 127px;
    font-family: "Arimo", sans-serif; font-size: 13px;
    letter-spacing: 3.4px; color: var(--brand-blue);
  }
  .phone {
    position: absolute; left: 320px; top: 154px;
    font-family: "Arimo", sans-serif; font-size: 26px;
    color: var(--slate); letter-spacing: 0.5px;
  }
  .hero {
    position: absolute; left: 0; top: 193px;
    width: 673px; height: 434px;
    background: linear-gradient(180deg, #2a78c6 0%, #6fa9d9 30%, #bfd3de 45%, #a9a394 60%, #b4ada0 100%);
  }
  .hero-photo-dog {
    position: absolute; right: 0; top: 0; width: 280px; height: 434px;
    background: linear-gradient(160deg, #5b6878 0%, #8b98a8 35%, #c99a52 60%, #dcae64 100%);
  }
  .headline {
    position: absolute; left: 52px; top: 54px;
    font-family: "Anton", sans-serif; font-size: 70px; line-height: 68px;
    color: var(--white); letter-spacing: -0.5px;
  }
  .services {
    position: absolute; left: 0; top: 627px;
    width: 673px; height: 261px; background: var(--band-blue);
  }
  .service {
    position: absolute; top: 31px; width: 177px; height: 200px; overflow: hidden;
  }
  .service:nth-child(1) { left: 28px; }
  .service:nth-child(2) { left: 248px; }
  .service:nth-child(3) { left: 467px; }
  .service-photo { width: 177px; height: 200px; }
  .photo-minding { background: linear-gradient(180deg, #9cc4e0 0%, #6f8f6a 45%, #5a9a32 100%); }
  .photo-visits { background: linear-gradient(180deg, #e8e6e2 0%, #c9c3bb 35%, #9a6f47 60%, #8a6038 100%); }
  .photo-walking { background: linear-gradient(180deg, #7d9a6e 0%, #6c8d58 40%, #d8c7ae 60%, #5f9a3a 100%); }
  .service-label {
    position: absolute; left: 0; bottom: 0; width: 177px; height: 32px;
    background: var(--label-grey); color: var(--white);
    font-family: "Arimo", sans-serif; font-size: 19px;
    display: flex; align-items: center; justify-content: center;
  }
  .footer {
    position: absolute; left: 0; top: 888px; width: 673px; height: 62px;
    display: flex; align-items: center; justify-content: center;
  }
  .website {
    font-family: "Arimo", sans-serif; font-size: 25px; color: var(--brand-blue);
  }
</style>
</head>
<body>
  <main class="poster">
    <header class="header">
      <span class="brand-mark"></span>
      <div class="brand-name">Pawfield<br>Haven</div>
      <div class="brand-tagline">PET SERVICES</div>
      <div class="phone">0400 555 318</div>
    </header>

    <section class="hero" role="img" aria-label="Golden retriever puppy leaning out of a car window at a sunny beach">
      <div class="hero-photo-dog"></div>
      <h1 class="headline">caring<br>for your<br>dog<br>like family</h1>
    </section>

    <section class="services">
      <div class="service">
        <div class="service-photo photo-minding" role="img" aria-label="Australian shepherd resting on green grass"></div>
        <div class="service-label">DOG MINDING</div>
      </div>
      <div class="service">
        <div class="service-photo photo-visits" role="img" aria-label="Small terrier sitting on a home doormat by the front door"></div>
        <div class="service-label">HOME VISITS</div>
      </div>
      <div class="service">
        <div class="service-photo photo-walking" role="img" aria-label="Bulldog on a lead standing in a park"></div>
        <div class="service-label">DOG WALKING</div>
      </div>
    </section>

    <footer class="footer">
      <div class="website">www.pawfieldhaven.com.au</div>
    </footer>
  </main>
</body>
</html>
```